Letterhead Design Project

Standard A4 paper, center the name Sparkwell Tidy (with the mop) same as front of business card.
748 Harbourview Rd Lindenvale 5087 ABN: 71326094518
M. 0428163904 T. 83917564 Calibri font

Industry/Entity Type

Business

```html
<!DOCTYPE html>
<html lang="en">
<head>
<meta charset="utf-8">
<title>Sparkwell Tidy Letterhead</title>
<link rel="stylesheet" href="https://fonts.googleapis.com/css2?family=Open+Sans:wght@400;700&display=swap">
<style>
  :root {
    --canvas: #ffffff;
    --page: #ffffff;
    --page-edge: #555555;
    --brand-blue: #3b3e8f;
    --rule-grey: #8e8e8e;
    --body-text: #333333;
    --abn-red: #e0393e;
    --mark-teal: #a6dadb;
  }
  * { margin: 0; padding: 0; box-sizing: border-box; }
  html, body {
    width: 1200px;
    height: 1002px;
    overflow: hidden;
    background: var(--canvas);
    font-family: "Open Sans", sans-serif;
  }
  .letterhead {
    position: absolute;
    left: 213px;
    top: 0;
    width: 775px;
    height: 1002px;
    background: var(--page);
    border: 1px solid var(--page-edge);
  }
  .brand-mark {
    position: absolute;
    left: 80px;
    top: 58px;
    width: 66px;
    height: 66px;
    background: var(--mark-teal);
  }
  .brand-name {
    position: absolute;
    left: 174px;
    top: 46px;
    width: 510px;
    font-size: 60px;
    font-weight: 700;
    line-height: 72px;
    letter-spacing: 1.5px;
    color: var(--brand-blue);
    text-align: center;
    white-space: nowrap;
  }
  .brand-rule {
    position: absolute;
    left: 180px;
    top: 113px;
    width: 498px;
    height: 7px;
    background: var(--rule-grey);
  }
  .contact-line {
    position: absolute;
    left: 180px;
    top: 122px;
    width: 498px;
    font-size: 13px;
    line-height: 18px;
    color: var(--body-text);
    text-align: center;
    white-space: nowrap;
  }
  .abn {
    position: absolute;
    right: 51px;
    top: 159px;
    font-size: 13px;
    line-height: 18px;
    color: var(--abn-red);
    white-space: nowrap;
  }
</style>
</head>
<body>
  <main class="letterhead">
    <div class="brand-mark" aria-hidden="true"></div>
    <h1 class="brand-name">SPARKWELL TIDY</h1>
    <div class="brand-rule"></div>
    <p class="contact-line">748, Harbourview Road, Lindenvale-5087&nbsp;&nbsp; Mob. 0428163904 T. 83917564</p>
    <p class="abn">ABN: 71326094518</p>
  </main>
</body>
</html>
```